Create the BEST and COOLEST website for events and media company!

Hi there. I am a start-up events and conferences company with a twist, and we are seeking a highly modern website for our company Quillfern Media. Our company believes that (like the social networking theory) that each and every one of us is connected to anyone on the planet in six connections or less. E.g. I know someone, who knows someone, who knows someone. Hence, the name Quillfern Media.

I have included the copy for the website attached.

While we do have a business audience, they are in the fields of technology from the banking, health, government sector. We would like our website to be edgy, fresh and steer away from stuffy corporate images.

To give you an idea, our website menu tabs will be labelled:
HOME: This will include a corporate video that’s being created next week for me. However, please still design this page with a very striking background image that fills the whole page. You can run the copy and put a mock video for me to just see the layout (we can insert the finished video later).

ROCKSTARS: this will show pictures of highly powerful leaders speaking on stage; with a highly engaged audience watching. We want to show we have the world’s best technology International speakers “rockstars” who are the best in their game when it comes to talking about the future of technology.

LOCAL LEGENDS: like the international ‘rockstar’ speakers we would bring over to Australia to present; this LOCAL LEGENDS page should show we have the best home-grown Chief business people speaking at conferences and smaller powerful roundtable luncheons.

UNSUNG HEROES: this is more the people in the audience who ask questions on a microphone; those that attend the conferences; or a speaking to people at a conference.

THE BAND: this is like an ‘about us’ – just a funkier name to tie in with the theme of rockstars, etc.

THE PARTNERS: this is like a sponsor client page, where we invite people to partner with us and sponsor our events and conferences.

YOU & DORIAN PELLHAM: Dorian Pellham is a famous actor who made the term ‘six degrees of separation’ very popular. This page will have a little bit of an introduction, but mainly have the following video fill the landing page: https://www.vidplume.example/watch?v=Tq4-zLp8XwE

Website Functionality and Features:

• Try and make the ‘vibe’ and look and feel consistent, hip and modern (but still maintain a professional look). At the end of the day, people looking at our website are very senior business chiefs of organisations and also marketing chiefs.
• We may add more pages once we become established, so the website needs to ensure we can do that easily.
• We want pictures to not look stock photos. We want them to fresh, innovative, inspirational.
• Images should have a ‘wow’ factor. Like this one: https://www.picharbor.example/detail/news-photo/general-view-of-atmosphere-during-brightloom-talks-2018-from-me-news-photo/481253907
• Need a mix of speaker, stage, audience, pictures. While we want to be fresh, edgy and contemporary we need to remember our viewers are the big chiefs of businesses – so lets try and have cool shots, but ensure there is a link to the business decision makers in a modern way. They all don’t have to wear suits, but not too casual either
• Other types of imagery I like is this one: https://www.picharbor.example/detail/photo/smiling-audience-using-smart-phone-flashlights-for-royalty-free-image/362817045.
• The following are ok, not wow – but to give you an idea:
• https://www.picharbor.example/detail/photo/smiling-male-speaker-in-wheelchair-on-stage-royalty-free-image/362819531
https://www.picharbor.example/detail/photo/smiling-woman-with-camera-phone-in-dark-audience-royalty-free-image/362818476
https://www.picharbor.example/detail/photo/audience-using-camera-phones-royalty-free-image/367402158
https://www.picharbor.example/detail/photo/male-speaker-on-stage-talking-to-audience-royalty-free-image/362818893

NB: Logos are supplied in low resolution, but I can send you high resolution also
Updates

Hi there I will be adding two low-resolution images of my business partner and I for the ABOUT US page which is called THE BAND in the menu tab.

Hi everyone, thank you for your designs. I have uploaded a MAIN SCREEN IDEAS word document to give you further ideas of how the options I like for the main landing page on the home page. Hope this helps!

Target Market(s)

High end business people in marketing and business.

Coding

Coded - Design and coding required

Number of Pages Required

5+ page

Font styles to use
Sans Serif

Requirements
Must have
• Fresh, inspirational and aspirational designs. We need to make events and conferences look exciting and that we are bring the best technology speakers (like Brightloom events) to our audience of marketing and technology professionals.
Should not have
• Cheesy, old stock photos; or pictures of American executives as this is for an Australian audience.
• PLEASE do not include an UPCOMING EVENTS or a SPEAKERS section as we will not be having this showcasing. You can feature ROCK STARS, LOCAL LEGENDS and UNSUNG HEROES if you like on the home page + the video of YOU and DORIAN PELLHAM (with his picture on the video box with a play button)

```html
<!DOCTYPE html>
<html lang="en">
<head>
<meta charset="utf-8">
<title>Quillfern Media — Events &amp; Conferences</title>
<link rel="stylesheet" href="https://fonts.googleapis.com/css2?family=Kanit:wght@300;400;500&family=Lato:ital,wght@0,400;0,700;1,400&display=swap">
<style>
:root{
  --navy:#131b5b;
  --navy-deep:#0f1650;
  --navy-line:#3a4388;
  --ink:#111111;
  --text:#222222;
  --muted:#555a66;
  --card:#eceef1;
  --panel:#f3f4f6;
  --white:#ffffff;
  --accent-red:#c8323a;
  --corner:#4b4f5a;
  --btn-blue:#2f5fd0;
}
*{box-sizing:border-box;margin:0;padding:0}
html,body{width:1200px;height:4178px;overflow:hidden}
body{background:var(--white);font-family:"Lato",sans-serif;color:var(--text);position:relative}
h1,h2,h3,h4{font-family:"Kanit",sans-serif;font-weight:400}
a{color:inherit;text-decoration:none}

/* Header */
.site-header{height:75px;display:flex;align-items:center;justify-content:space-between;padding:0 100px 0 130px;background:var(--white)}
.brand{display:flex;align-items:center;gap:10px}
.brand-dot{width:26px;height:26px;border-radius:50%;background:var(--ink)}
.brand-name{font-family:"Kanit",sans-serif;font-weight:400;font-size:19px;color:var(--ink)}
.main-nav{display:flex;gap:4px}
.main-nav a{font-family:"Kanit",sans-serif;font-size:13px;color:var(--ink);padding:8px 10px;letter-spacing:.2px}
.main-nav a.is-active{background:var(--ink);color:var(--white)}

/* Hero */
.hero{position:relative;height:678px}
.hero-media{position:absolute;inset:0;background:
  radial-gradient(ellipse 420px 520px at 820px 330px,#8c7a74 0%,#4a3d42 45%,transparent 75%),
  linear-gradient(100deg,#1b2a6b 0%,#3a1e3c 30%,#6a1c24 50%,#2a1a22 70%,#120f18 100%)}
.play-button{position:absolute;left:452px;top:285px;width:156px;height:156px}

.info-cards{position:absolute;left:128px;top:609px;display:flex;gap:28px}
.info-card{width:296px;height:226px;background:var(--card);text-align:center;padding-top:42px}
.info-card svg{width:50px;height:50px}
.info-card h3{font-size:27px;margin-top:8px;color:var(--ink)}
.info-card p{font-size:14px;font-weight:700;margin-top:10px;color:var(--ink)}

/* Band */
.band{position:absolute;top:982px;left:0;width:1200px;height:525px;display:flex}
.band-photo{width:550px;height:525px;background:linear-gradient(160deg,#3a2418 0%,#6b4630 35%,#c9c3bb 60%,#2b2420 100%)}
.band-copy{width:500px;margin-left:28px;padding-top:6px}
.band-copy h2{font-size:30px;color:var(--ink);letter-spacing:.5px}
.lead{font-style:italic;color:var(--navy);font-size:16px;line-height:20px;margin-top:22px}
.band-copy .body{font-size:13px;line-height:19px;margin-top:14px;color:var(--text)}
.btn-dark{display:inline-block;margin-top:22px;margin-left:8px;background:var(--ink);color:var(--white);font-family:"Kanit",sans-serif;font-size:18px;padding:8px 20px;letter-spacing:.5px}

/* About */
.about{position:absolute;top:1593px;left:0;width:1200px;height:776px;background:var(--navy);color:var(--white);text-align:center}
.about h2{font-size:34px;letter-spacing:1px;margin-top:42px}
.about .lead{color:#dfe3ff;margin:22px auto 0;width:780px}
.value-grid{display:grid;grid-template-columns:repeat(3,296px);gap:36px 28px;justify-content:center;margin-top:70px}
.value-card{height:223px;border:1px solid var(--navy-line);padding-top:20px}
.value-card svg{width:70px;height:70px}
.value-card h3{font-size:22px;font-weight:300;margin-top:6px}
.value-card p{font-size:14px;font-weight:700;line-height:18px;margin:8px auto 0;width:250px}

/* Partners */
.partners{position:absolute;top:2369px;left:0;width:1200px;height:605px;text-align:center}
.partners h2{font-size:34px;color:var(--ink);margin-top:70px;letter-spacing:.5px}
.partners .lead{margin:16px auto 0;width:780px}
.partner-grid{display:flex;gap:28px;justify-content:center;margin-top:50px}
.partner-card{position:relative;width:296px;height:335px;background:var(--card);overflow:hidden;padding-top:28px}
.partner-card::before{content:"";position:absolute;right:0;top:0;border-top:80px solid var(--corner);border-left:80px solid transparent}
.partner-card::after{content:"";position:absolute;left:0;bottom:0;border-bottom:80px solid var(--corner);border-right:80px solid transparent}
.portrait{position:relative;z-index:1;width:142px;height:142px;margin:0 auto;border-radius:50%;border:6px solid var(--navy);background:radial-gradient(circle at 50% 40%,#c9c9cc,#8a8d94)}
.partner-card h3{font-size:24px;color:var(--navy);margin-top:14px;font-weight:300}
.role{font-size:12px;margin-top:4px;color:var(--ink)}
.partner-card .bio{font-size:12px;line-height:16px;margin:12px auto 0;width:250px}
.dots{display:flex;gap:6px;justify-content:center;margin-top:10px;position:relative;z-index:1}
.dots span{width:11px;height:11px;border-radius:50%;background:var(--navy)}

/* Register */
.register{position:absolute;top:2974px;left:0;width:1200px;height:355px;text-align:center;color:var(--white);
  background:linear-gradient(rgba(20,28,92,.82),rgba(20,28,92,.82)),linear-gradient(120deg,#6b5a48,#2b2a33 45%,#7a6a56 80%,#3b3640)}
.register h2{font-size:40px;font-weight:300;letter-spacing:2px;padding-top:58px}
.register p{font-family:"Kanit",sans-serif;font-size:22px;font-weight:300;margin-top:4px}
.btn-outline{display:inline-block;margin-top:38px;border:2px solid var(--btn-blue);color:var(--white);font-family:"Kanit",sans-serif;font-size:27px;padding:10px 30px;background:rgba(15,22,80,.6)}

/* Services */
.services{position:absolute;top:3329px;left:0;width:1200px;height:471px;background:var(--panel);text-align:center}
.services h2{font-size:36px;color:var(--ink);margin-top:58px}
.service-grid{display:flex;gap:28px;justify-content:center;margin-top:58px}
.service-card{width:296px}
.service-photo{height:193px}
.service-card h3{font-size:21px;font-weight:400;color:var(--ink);margin-top:26px}

/* Footer */
.site-footer{position:absolute;top:3800px;left:0;width:1200px;height:378px;background:var(--navy-deep);color:var(--white)}
.footer-cols{position:relative;height:320px}
.footer-col{position:absolute;top:72px}
.footer-col h4{font-size:17px;margin-bottom:20px}
.footer-col p{font-size:11px;line-height:20px}
.footer-col li{list-style:none;font-size:11px;line-height:30px}
.footer-col .socials{display:flex;gap:8px;margin-top:14px}
.footer-col .socials span{width:14px;height:14px;border-radius:50%;background:var(--white)}
.contact li{display:flex;align-items:center;gap:8px;line-height:34px}
.contact svg{width:16px;height:16px}
.footer-bottom{position:absolute;left:130px;right:130px;top:324px;border-top:1px solid var(--navy-line);text-align:center;font-size:10px;padding-top:20px}
</style>
</head>
<body>

<header class="site-header">
  <a class="brand" href="#"><span class="brand-dot"></span><span class="brand-name">Quillfern Media</span></a>
  <nav class="main-nav">
    <a class="is-active" href="#">HOME</a>
    <a href="#">ROCKSTARS</a>
    <a href="#">LOCAL LEGENDS</a>
    <a href="#">UNSUNG HEROES</a>
    <a href="#">THE BAND</a>
    <a href="#">THE PARTNERS</a>
    <a href="#">YOU &amp; DORIAN PELLHAM</a>
  </nav>
</header>

<section class="hero">
  <div class="hero-media" role="img" aria-label="Speaker with headset microphone on stage before a packed conference audience"></div>
  <svg class="play-button" viewBox="0 0 156 156" aria-label="Play video">
    <circle cx="78" cy="78" r="78" fill="var(--accent-red)" opacity=".9"/>
    <path d="M60 46 L110 78 L60 110 Z" fill="#e8e8ec"/>
  </svg>
  <div class="info-cards">
    <div class="info-card">
      <svg viewBox="0 0 50 50" fill="none" stroke="#111" stroke-width="3"><rect x="6" y="9" width="38" height="35" rx="3"/><path d="M6 18h38M15 4v9M35 4v9"/><g fill="#111" stroke="none"><rect x="12" y="23" width="5" height="5"/><rect x="22" y="23" width="5" height="5"/><rect x="32" y="23" width="5" height="5"/><rect x="12" y="33" width="5" height="5"/><rect x="22" y="33" width="5" height="5"/><rect x="32" y="33" width="5" height="5"/></g></svg>
      <h3>Event Date</h3>
      <p>Thursday, January 31, 2019</p>
    </div>
    <div class="info-card">
      <svg viewBox="0 0 50 50"><path d="M25 3c-9 0-16 7-16 16 0 12 16 28 16 28s16-16 16-28c0-9-7-16-16-16z" fill="#111"/><circle cx="25" cy="19" r="6" fill="var(--card)"/></svg>
      <h3>Event Location</h3>
      <p>New South Wales</p>
    </div>
    <div class="info-card">
      <svg viewBox="0 0 50 50" fill="#111"><circle cx="25" cy="15" r="10"/><path d="M6 47c0-11 8-18 19-18s19 7 19 18z"/></svg>
      <h3>Send Us a Mail</h3>
      <p>info@quillfernmedia.com.au</p>
    </div>
  </div>
</section>

<section class="band">
  <div class="band-photo" role="img" aria-label="Executives seated along a long table at a roundtable luncheon"></div>
  <div class="band-copy">
    <h2>THE BAND</h2>
    <p class="lead">Lorem ipsum dolor sit amet, consectetur adipiscing elit. Quisque auctor ligula quis ultrices commodo. Maecenas vitae neque id est laoreet luctus</p>
    <p class="body">Lorem ipsum dolor sit amet, con aipis icing elit, sed do eiusmod tempor-Lorem ipsum dolor sit amet.Lorem ipsum dolor sit amet, con aipis icing elit, sed do eiusmod temporLorem ipsum dolor sit amet.Lorem ipsum dolor sit amet, con aipis icing elit, sed do eiusmod temporLorem ipsum dolor sit amet.Lorem ipsum dolor sit amet, con aipis icing elit, sed do eiusmod temporLorem ipsum dolor sit amet.Lorem ipsum dolor sit amet, con aipis icing elit, sed do eiusmod temporLorem ipsum dolor sit amet.Lorem ipsum dolor sit amet, con aipis icing elit, sed do eiusmod temporLorem ipsum dolor sit amet.Lorem ipsum dolor sit amet, con aipis icing elit, sed do eiusmod temporLorem ipsum dolor sit amet.Lorem ipsum dolor sit amet, con aipis icing elit, sed do eiusmod temporLorem ipsum dolor sit amet.</p>
    <a class="btn-dark" href="#">Know More</a>
  </div>
</section>

<section class="about">
  <h2>QUILLFERN MEDIA</h2>
  <p class="lead">Lorem ipsum dolor sit amet, consectetur adipiscing elit. Quisque auctor ligula quis ultrices commodo. Maecenas vitae neque id est laoreet luctus</p>
  <div class="value-grid">
    <div class="value-card">
      <svg viewBox="0 0 70 70" fill="none" stroke="#fff" stroke-width="2.5"><circle cx="35" cy="35" r="24"/><circle cx="35" cy="35" r="10"/></svg>
      <h3>Our Philosophy</h3>
      <p>Lorem ipsum dolor sit amet, con aipis icing elit, sed do eiusmod tempor</p>
    </div>
    <div class="value-card">
      <svg viewBox="0 0 70 70" fill="none" stroke="#fff" stroke-width="2.5"><circle cx="35" cy="16" r="7"/><circle cx="14" cy="48" r="7"/><circle cx="56" cy="48" r="7"/><path d="M29 22 18 41M41 22l11 19M21 50h28"/></svg>
      <h3>Join Us</h3>
      <p>Lorem ipsum dolor sit amet, con aipis icing elit, sed do eiusmod tempor</p>
    </div>
    <div class="value-card">
      <svg viewBox="0 0 70 70" fill="none" stroke="#fff" stroke-width="2.5"><path d="M10 12h30v20H22l-8 7v-7h-4z"/><path d="M44 28h16v20h-4v7l-8-7H30V38"/></svg>
      <h3>Comunity</h3>
      <p>Lorem ipsum dolor sit amet, con aipis icing elit, sed do eiusmod tempor</p>
    </div>
    <div class="value-card">
      <svg viewBox="0 0 70 70" fill="none" stroke="#fff" stroke-width="2.5"><path d="M8 30l14-14 10 6 8-4 14 14-16 18-10-4-6 4z"/><path d="M26 36l8 8M32 32l8 8"/></svg>
      <h3>Motivation</h3>
      <p>Lorem ipsum dolor sit amet, con aipis icing elit, sed do eiusmod tempor</p>
    </div>
    <div class="value-card">
      <svg viewBox="0 0 70 70" fill="none" stroke="#fff" stroke-width="2.5"><circle cx="35" cy="18" r="7"/><circle cx="17" cy="26" r="6"/><circle cx="53" cy="26" r="6"/><path d="M24 58V36h22v22M8 58V40h12M62 58V40H50"/></svg>
      <h3>Our People</h3>
      <p>Lorem ipsum dolor sit amet, con aipis icing elit, sed do eiusmod tempor</p>
    </div>
    <div class="value-card">
      <svg viewBox="0 0 70 70" fill="none" stroke="#fff" stroke-width="2.5"><path d="M10 26 20 12h30l10 14-25 32z"/><path d="M10 26h50M28 12l-4 14 11 32 11-32-4-14"/></svg>
      <h3>Our Work</h3>
      <p>Lorem ipsum dolor sit amet, con aipis icing elit, sed do eiusmod tempor</p>
    </div>
  </div>
</section>

<section class="partners">
  <h2>THE PARTNERS</h2>
  <p class="lead">Lorem ipsum dolor sit amet, consectetur adipiscing elit. Quisque auctor ligula quis ultrices commodo. Maecenas vitae neque id est laoreet luctus</p>
  <div class="partner-grid">
    <div class="partner-card">
      <div class="portrait" role="img" aria-label="Portrait of partner Andrive Doe"></div>
      <h3>Andrive Doe</h3>
      <p class="role">Speaker</p>
      <p class="bio">Lorem ipsum dolor sit amet, con aipis icing elit, sed do eiusmod tempor</p>
      <div class="dots"><span></span><span></span><span></span></div>
    </div>
    <div class="partner-card">
      <div class="portrait" role="img" aria-label="Portrait of partner Erica Semi"></div>
      <h3>Erica Semi</h3>
      <p class="role">Speaker</p>
      <p class="bio">Lorem ipsum dolor sit amet, con aipis icing elit, sed do eiusmod tempor</p>
      <div class="dots"><span></span><span></span><span></span></div>
    </div>
    <div class="partner-card">
      <div class="portrait" role="img" aria-label="Portrait of partner Martin Jamil"></div>
      <h3>Martin Jamil</h3>
      <p class="role">Speaker</p>
      <p class="bio">Lorem ipsum dolor sit amet, con aipis icing elit, sed do eiusmod tempor</p>
      <div class="dots"><span></span><span></span><span></span></div>
    </div>
  </div>
</section>

<section class="register" role="img" aria-label="Large conference audience seated in a hall, tinted navy">
  <h2>ENJOY THE EVENT</h2>
  <p>Top Leaders Knowledge and Experience</p>
  <a class="btn-outline" href="#">Register Now</a>
</section>

<section class="services">
  <h2>OUR SERVICES</h2>
  <div class="service-grid">
    <div class="service-card">
      <div class="service-photo" role="img" aria-label="Business event with delegates around meeting tables" style="background:linear-gradient(135deg,#e8e4de,#8a7a6a 55%,#3a3230)"></div>
      <h3>Business Events</h3>
    </div>
    <div class="service-card">
      <div class="service-photo" role="img" aria-label="Motivational event with speaker addressing an engaged audience" style="background:linear-gradient(135deg,#5a3a26,#a8663a 50%,#2a1c16)"></div>
      <h3>Motivational Events</h3>
    </div>
    <div class="service-card">
      <div class="service-photo" role="img" aria-label="Social event crowd raising hands in a lit venue" style="background:linear-gradient(135deg,#8a5a30,#4a3024 50%,#1e1612)"></div>
      <h3>Social Events</h3>
    </div>
  </div>
</section>

<footer class="site-footer">
  <div class="footer-cols">
    <div class="footer-col" style="left:130px;width:270px">
      <h4>About Us</h4>
      <p>Lorem ipsum dolor sit amet, con aipis icing elit, sed do eiusmod temporLorem ipsum dolor sit amet.Lorem ipsum dolor sit amet, con aipis icing elit, sed do eiusmod tempor-Lorem ipsum dolor sit amet.</p>
      <div class="socials"><span></span><span></span><span></span><span></span></div>
    </div>
    <div class="footer-col" style="left:432px">
      <h4>Our Services</h4>
      <ul><li>Business Events</li><li>Motivational Events</li><li>Social Events</li><li>Lorem Ipsum</li><li>Dolor Sit</li></ul>
    </div>
    <div class="footer-col" style="left:639px">
      <h4>Quick Links</h4>
      <ul style="line-height:1"><li style="line-height:30px">Home</li><li style="line-height:30px">Rockstars</li><li style="line-height:30px">Local Legends</li><li style="line-height:30px">Unsung Heroes</li><li style="line-height:30px">The Band</li><li style="line-height:30px">The Partners</li><li style="line-height:30px">You &amp; Dorian Pellham</li></ul>
    </div>
    <div class="footer-col contact" style="left:837px">
      <h4>Contact Us</h4>
      <ul>
        <li><svg viewBox="0 0 16 16"><rect width="16" height="16" rx="3" fill="#fff"/><path d="M8 3a3.5 3.5 0 0 0-3.5 3.5C4.5 9 8 13 8 13s3.5-4 3.5-6.5A3.5 3.5 0 0 0 8 3z" fill="var(--navy-deep)"/></svg>301 Lorem ipsum dolor</li>
        <li><svg viewBox="0 0 16 16"><rect width="16" height="16" rx="3" fill="#fff"/><rect x="5" y="2.5" width="6" height="11" rx="1" fill="var(--navy-deep)"/></svg>00 123 456 789</li>
        <li><svg viewBox="0 0 16 16"><rect width="16" height="16" rx="3" fill="#fff"/><path d="M4 3h3l1 3-2 1a7 7 0 0 0 3 3l1-2 3 1v3c-5 1-10-4-9-9z" fill="var(--navy-deep)"/></svg>00 123 456 789</li>
        <li><svg viewBox="0 0 16 16"><rect width="16" height="16" rx="3" fill="#fff"/><rect x="3" y="4.5" width="10" height="7" fill="var(--navy-deep)"/><path d="M3 4.5l5 4 5-4" stroke="#fff" fill="none"/></svg>info@quillfernmedia.com.au</li>
      </ul>
    </div>
  </div>
  <div class="footer-bottom">Copyright © 2019 quillfernmedia.com.au. All Rights Reserved</div>
</footer>

</body>
</html>
```